Bright Pelvic Health Business Card

Need a business card for a surgical practice called Bright Pelvic Health. We have recently selected a logo (attached). The business card will need to have two formats:
1) One with the logo/physician name/ contact info on the front and location information on the back.
2) One in "appointment reminder card" style with the logo/ contact info/ date/ time on the front and the location information on the back.

The front side should include the following information:
- Logo
- Ravi K. Desai, MD FACOG
- phone: 469-555-0182
- fax: 1-469-555-0147
- email: admin@brightpelvic.example
- website: www.brightpelvichealth.example

The back side should have the office locations listed:
4812 Quarry Bend Dr, Frisco, TX 75034
3650 Wrenfield Rd, McKinney, TX 75070
2245 Brambleton Ln, Garland, TX 75040
915 S Garnet Ave B314, Denton, TX 76201
1836 Tillman Pkwy, Mesquite, TX 75149
6417 Dorrance Way Dr, Austin, TX 78745
5920 Kessler Rd, Waco, TX 76710

Target Market(s)

1. Other physicians who might refer patients
2. Female patients

Industry/Entity Type

Business

Font styles to use
Other font styles liked:
• Tahoma for lettering

Requirements
Must have
• As per the instructions
Should not have
• No other images needed -- please try to keep font consistent with logo design. Can use Tahoma as the font for lettering.

```html
<!DOCTYPE html>
<html lang="en">
<head>
<meta charset="utf-8">
<title>Bright Pelvic Health – Business Card</title>
<link rel="stylesheet" href="https://fonts.googleapis.com/css2?family=Michroma&family=PT+Sans:wght@400;700&display=swap">
<style>
  :root {
    --page: #ffffff;
    --band-edge: #1c3a86;
    --band-mid: #8a9bc6;
    --band-center: #f4f5fa;
    --panel: #29186e;
    --ink-gold: #f2ea1c;
    --brand-blue: #2a4f9e;
    --tag-blue: #3a5aa6;
  }
  * { margin: 0; padding: 0; box-sizing: border-box; }
  html, body {
    width: 994px; height: 1200px; overflow: hidden;
    background: var(--page);
  }
  .sheet { position: relative; width: 994px; height: 1200px; }
  .card {
    position: absolute; left: 123px; width: 792px;
    border-radius: 24px 24px 38px 38px; overflow: hidden;
    background: var(--page);
  }
  .card--front { top: 75px; height: 515px; }
  .card--back { top: 623px; height: 514px; }
  .card__band {
    position: absolute; left: 0; right: 0; top: 0;
    background:
      radial-gradient(ellipse 30% 70% at 50% 100%, rgba(244,245,250,0.9) 0%, rgba(244,245,250,0) 100%),
      linear-gradient(90deg, var(--band-edge) 0%, var(--band-mid) 28%, var(--band-center) 50%, var(--band-mid) 72%, var(--band-edge) 100%);
    display: flex; flex-direction: column; align-items: center;
  }
  .card--front .card__band { height: 195px; padding-top: 116px; }
  .card--back .card__band { height: 184px; justify-content: center; }
  .card__panel {
    position: absolute; left: 0; right: 0; bottom: 0;
    background: var(--panel);
    display: flex; flex-direction: column; align-items: center; justify-content: center;
    color: var(--ink-gold);
    font-family: "Michroma", "PT Sans", sans-serif;
    font-variant: small-caps;
    -webkit-text-stroke: 0.4px var(--ink-gold);
    text-align: center;
  }
  .card--front .card__panel { top: 205px; padding-bottom: 70px; }
  .card--back .card__panel { top: 195px; padding-bottom: 30px; }
  .brand {
    display: flex; align-items: center; gap: 10px;
    font-family: "PT Sans", sans-serif; font-weight: 700;
    color: var(--brand-blue); line-height: 1;
  }
  .brand__mark {
    width: 14px; height: 14px; border-radius: 50%; background: var(--brand-blue);
  }
  .card--front .brand { font-size: 29px; }
  .card--back .brand { font-size: 30px; }
  .brand__tagline {
    font-family: "PT Sans", sans-serif; font-size: 27px; line-height: 1;
    color: var(--tag-blue); margin-top: 4px;
  }
  .contact { list-style: none; font-size: 15px; line-height: 24px; letter-spacing: 0.6px; }
  .contact__name { font-size: 17px; }
  .locations { list-style: none; font-size: 14px; line-height: 23px; letter-spacing: 0.6px; }
</style>
</head>
<body>
<main class="sheet">
  <section class="card card--front">
    <header class="card__band">
      <div class="brand"><span class="brand__mark"></span><span class="brand__name">Bright Pelvic Health</span></div>
      <p class="brand__tagline">calm.....the.....core</p>
    </header>
    <div class="card__panel">
      <ul class="contact">
        <li class="contact__name">Ravi K. Desai, MD FACOG</li>
        <li>phone: 469-555-0182</li>
        <li>fax:1-469-555-0147</li>
        <li>email: admin@brightpelvic.example</li>
        <li>website: www.brightpelvichealth.example</li>
      </ul>
    </div>
  </section>

  <section class="card card--back">
    <header class="card__band">
      <div class="brand"><span class="brand__mark"></span><span class="brand__name">Bright Pelvic Health</span></div>
    </header>
    <div class="card__panel">
      <ul class="locations">
        <li>4812 Quarry Bend Dr, Frisco, TX 75034</li>
        <li>3650 Wrenfield Rd, McKinney, TX 75070</li>
        <li>2245 Brambleton Ln, Garland, TX 75040</li>
        <li>915 S Garnet Ave B314, Denton, TX 76201</li>
        <li>1836 Tillman Pkwy, Mesquite, TX 75149</li>
        <li>6417 Dorrance Way Dr, Austin, TX 78745</li>
        <li>5920 Kessler Rd, Waco, TX 76710</li>
      </ul>
    </div>
  </section>
</main>
</body>
</html>
```